Drag Show Flyer

We are holding a Drag Show, we are looking for something fun and exciting, over the top is a must.

Show Date: Saturday September 2nd 2017
Venue: Pelican Row Cafe Bunbury
Doors open 7pm
Tickets: $50 per person, includes glass of sparkling on arrival and canapes
Tickets available at the Venue or from ticketloom.com.au

Target Market(s)

Female, Hens Party, LBGT

Industry/Entity Type

Entertainment

Colors

Designer to choose colors to be used in the design.

Requirements
Must have
• Show Date: Saturday September 2nd 2017
• Venue: Pelican Row Cafe Bunbury
• Doors open 7pm
• Tickets: $50 per person, includes glass of sparkling on arrival and canapes
• Tickets available at the Venue or from ticketloom.com.au

```html
<!DOCTYPE html>
<html lang="en">
<head>
<meta charset="utf-8">
<title>Drag Show – Pelican Row Cafe Bunbury</title>
<link rel="stylesheet" href="https://fonts.googleapis.com/css2?family=Open+Sans:wght@700;800&family=Arimo:wght@400;700&display=swap">
<style>
  :root {
    --night: #0b0f12;
    --ink-outline: #2b0d08;
    --white: #ffffff;
    --paper: #ffffff;
    --text-dark: #111111;
    --alert-red: #e0100c;
    --line-glow: #fff8d0;
  }
  * { margin: 0; padding: 0; box-sizing: border-box; }
  html, body { width: 872px; height: 1200px; overflow: hidden; background: var(--paper); }
  .flyer {
    position: relative;
    width: 872px;
    height: 1200px;
    overflow: hidden;
    font-family: "Open Sans", Arial, sans-serif;
  }
  .stage {
    position: absolute;
    left: 0; top: 0;
    width: 872px; height: 988px;
    background:
      radial-gradient(ellipse 260px 240px at 440px 390px, rgba(255,214,60,0.95), rgba(240,150,20,0.55) 45%, rgba(0,0,0,0) 80%),
      radial-gradient(ellipse 520px 320px at 440px 150px, rgba(40,150,140,0.85), rgba(20,70,70,0.4) 55%, rgba(0,0,0,0) 85%),
      radial-gradient(ellipse 620px 260px at 520px 800px, rgba(210,20,10,0.9), rgba(120,8,4,0.6) 55%, rgba(0,0,0,0) 90%),
      radial-gradient(ellipse 500px 220px at 780px 560px, rgba(220,40,10,0.7), rgba(0,0,0,0) 80%),
      var(--night);
  }
  .stage-lines { position: absolute; left: 0; top: 0; }
  .performer-photo {
    position: absolute;
    left: 336px; top: 70px;
    width: 254px; height: 520px;
    border-radius: 120px 120px 40px 40px;
    background: linear-gradient(180deg, #2a1208 0%, #8a4a1c 30%, #d6961e 55%, #c46a12 78%, rgba(180,60,10,0) 100%);
    opacity: 0.9;
  }
  .headline {
    position: absolute;
    left: 10px; width: 872px;
    text-align: center;
    font-weight: 800;
    font-size: 160px;
    line-height: 1;
    letter-spacing: -3px;
    color: var(--white);
    -webkit-text-stroke: 22px var(--ink-outline);
    paint-order: stroke fill;
  }
  .headline-drag { top: 372px; }
  .headline-show { top: 500px; }
  .show-day, .show-date {
    position: absolute; width: 872px; text-align: center;
    font-weight: 700; color: var(--white); line-height: 1;
  }
  .show-day { top: 676px; font-size: 44px; left: 8px; }
  .show-date { top: 730px; font-size: 46px; left: 12px; }
  .show-date sup { font-size: 24px; vertical-align: 20px; }
  .divider {
    position: absolute; left: 268px; top: 792px;
    width: 352px; height: 1px; background: rgba(255,255,255,0.85);
  }
  .venue {
    position: absolute; left: 0; width: 872px; top: 802px;
    text-align: center; font-weight: 700; font-size: 24px; color: var(--white);
  }
  .doors {
    position: absolute; left: 0; width: 872px; top: 850px;
    text-align: center; font-family: "Arimo", Arial, sans-serif;
    font-weight: 700; font-size: 66px; color: var(--white); line-height: 1;
  }
  .ticket-band {
    position: absolute; left: 0; top: 988px;
    width: 872px; height: 212px; background: var(--paper);
  }
  .ticket-price {
    position: absolute; left: 0; width: 872px; top: 1014px;
    text-align: center; font-weight: 800; font-size: 16px; color: var(--text-dark);
    text-transform: uppercase;
  }
  .ticket-outlets {
    position: absolute; left: 0; width: 872px; top: 1038px;
    text-align: center; font-family: "Arimo", Arial, sans-serif;
    font-weight: 700; font-size: 19px; color: var(--alert-red);
  }
  .partners {
    position: absolute; left: 0; top: 1100px;
    width: 872px; height: 60px;
  }
  .partner {
    position: absolute; top: 0; width: 200px; height: 60px;
    display: flex; align-items: center; justify-content: center;
    text-align: center;
    font-weight: 700; font-size: 18px; color: var(--text-dark); line-height: 1.15;
  }
  .partner-venue { left: 147px; }
  .partner-group { left: 356px; }
  .partner-productions { left: 526px; }
</style>
</head>
<body>
<main class="flyer">
  <section class="stage">
    <div class="performer-photo" role="img" aria-label="Photo of the drag performer in a gold sequin top with long dark hair"></div>
    <svg class="stage-lines" width="872" height="988" viewBox="0 0 872 988" aria-hidden="true">
      <g fill="none" stroke="var(--line-glow)" stroke-width="3" opacity="0.9">
        <polygon points="521,80 196,372 646,228"/>
        <polygon points="277,142 600,148 620,400"/>
      </g>
    </svg>
    <div class="headline headline-drag">Drag</div>
    <div class="headline headline-show">Show</div>
    <div class="show-day">Saturday</div>
    <div class="show-date">September 2<sup>nd</sup> 2017</div>
    <div class="divider"></div>
    <div class="venue">Pelican Row Cafe Bunbury</div>
    <div class="doors">Doors open 7pm</div>
  </section>
  <section class="ticket-band"></section>
  <p class="ticket-price">Tickets: $50 per person, includes glass of sparkling on arrival and canapes</p>
  <p class="ticket-outlets">Tickets available at the Venue or from ticketloom.com.au</p>
  <footer class="partners">
    <div class="partner partner-venue">Pelican Row</div>
    <div class="partner partner-group">Brightline<br>Group</div>
    <div class="partner partner-productions">Chatterbox<br>Productions</div>
  </footer>
</main>
</body>
</html>
```